Velmora EIRL Business Card Design Project

We need a business card design for a New Business Intelligence Consultant. We bring a complete service to the client from first consulting meeting to help desk and system improvement.

I will upload the company logo and I like to use the logo colors on the card. Feel free to use all logo components on the design, for example one side with the black logo using complete card and the other side only the red shape (is an example, feel absolutely free :)).

The principal idea is to sell a professional service and a modern company.

Target Market(s)

IT Business Intelligence Clients

Industry/Entity Type

Professional Service

Requirements
Nice to have
• - Use the logo colors and minimize white sections.
- Rounded borders
Should not have
• I don't want to see any references to people working on a meeting or office photos or any computers related logos.

```html
<!DOCTYPE html>
<html lang="en">
<head>
<meta charset="utf-8">
<title>Velmora EIRL – Business Card</title>
<link rel="stylesheet" href="https://fonts.googleapis.com/css2?family=Barlow:ital,wght@0,400;0,500;0,600;1,400&display=swap">
<style>
  :root {
    --ink: #000000;
    --paper: #ffffff;
    --brand-red: #ed1c24;
    --brand-grey: #939598;
    --brand-grey-dark: #6d6e71;
    --text-dark: #231f20;
    --faint-grey: #ececec;
  }
  * { margin: 0; padding: 0; box-sizing: border-box; }
  html, body {
    width: 1050px; height: 1200px; overflow: hidden;
    background: var(--paper);
    font-family: "Barlow", sans-serif;
  }
  .canvas { position: relative; width: 1050px; height: 1200px; }

  /* Front side */
  .card-front {
    position: absolute; left: 0; top: 0; width: 1050px; height: 600px;
    background: var(--ink);
    display: flex; align-items: center; justify-content: center; gap: 40px;
  }
  .brand-mark { display: block; background: var(--brand-red); }
  .card-front .brand-mark { width: 120px; height: 120px; }
  .brand-name {
    font-weight: 500; color: var(--brand-red); line-height: 1;
    letter-spacing: 1px;
  }
  .card-front .brand-name { font-size: 150px; margin-top: -14px; }

  /* Back side */
  .card-back {
    position: absolute; left: 0; top: 600px; width: 1050px; height: 600px;
    background: var(--paper); overflow: hidden;
  }
  .back-accent {
    position: absolute; left: 40px; top: 60px; width: 440px; height: 440px;
    background: var(--faint-grey); opacity: .6;
  }
  .back-brand {
    position: absolute; right: 70px; top: 62px;
    display: flex; align-items: center; gap: 28px;
  }
  .back-brand .brand-mark { width: 80px; height: 80px; }
  .back-brand .brand-name { font-size: 100px; margin-top: -10px; }

  .identity { position: absolute; right: 62px; top: 192px; text-align: right; }
  .person-name {
    font-size: 50px; font-weight: 400; color: var(--brand-grey-dark);
    letter-spacing: 1px; line-height: 1;
  }
  .person-role {
    font-size: 27px; font-style: italic; color: var(--brand-grey-dark);
    letter-spacing: 1px; margin-top: 10px;
  }

  .contact {
    position: absolute; right: 62px; top: 318px; text-align: right;
    list-style: none; font-size: 28px; line-height: 37.6px;
    color: var(--text-dark); letter-spacing: .8px;
  }
  .contact .web { color: var(--brand-red); font-weight: 600; }
</style>
</head>
<body>
<main class="canvas">
  <section class="card-front">
    <span class="brand-mark" aria-hidden="true"></span>
    <span class="brand-name">velmora</span>
  </section>

  <section class="card-back">
    <div class="back-accent" aria-hidden="true"></div>

    <div class="back-brand">
      <span class="brand-mark" aria-hidden="true"></span>
      <span class="brand-name">velmora</span>
    </div>

    <div class="identity">
      <p class="person-name">Name Representative</p>
      <p class="person-role">Corporate Sales Manager</p>
    </div>

    <ul class="contact">
      <li>5120 NW 87TH AVE.</li>
      <li>Doral, Florida. 33178</li>
      <li>Ofic.: 000-000-0000</li>
      <li>Cel.: 000-000-0000</li>
      <li>email: info@velmora.com</li>
      <li class="web">www.velmora.com</li>
    </ul>
  </section>
</main>
</body>
</html>
```